Moderne CI für einen Immobilienmakler [www.terbek-wohnwerte.de]
Zielgruppe
Kunden für hochwertige Immobilien, also gemischtes eher anspruchvolles Klientel.
Hallo,
ich betreibe ein junges Immobilienunternehmen im 4. Geschäftsjahr. Wir vermarkten ausschließlich hochwertige Immobilien. Meine derzeitiges Logo habe ich damals selbst entworfen und es harmoniert gut mit meiner Website [www.terbek-wohnwerte.de] leider habe ich für Printmedien nie eine CI hinbekommen die mir richtig gefällt und die im Gesamt- und Farbkonzept zu meinem Onlineauftritt passt.
Ich wünsche mir nun von einem professionellen Designer eine modern- edle CI mit Entwürfen für Briefpapier, Umschläge C4 und DL, A4 Exposé-Mappe sowie die Rohlinge für eine Dreiseiter Image-Broschüre, für ein Objekt Expose sowie für eine Print-Annonce.
Eine spätere Zusammenarbeit für weitere Medien ist erwünscht.

```html
<!DOCTYPE html>
<html lang="de">
<head>
<meta charset="utf-8">
<title>terbek wohnwerte – Visitenkarte</title>
<link rel="stylesheet" href="https://fonts.googleapis.com/css2?family=Arimo:wght@400;700&display=swap">
<style>
  :root {
    --page-bg: #ececec;
    --card-white: #ffffff;
    --card-grey-top: #f4f4f4;
    --card-grey-bottom: #cfcfcf;
    --back-grey-top: #d2d2d2;
    --back-grey-bottom: #bdbdbd;
    --text-dark: #1e1e1e;
    --text-grey: #555555;
    --brand-grey: #6f6f6f;
    --accent-red: #e3141b;
    --card-shadow: rgba(0, 0, 0, 0.18);
  }
  html, body {
    margin: 0;
    padding: 0;
    width: 1200px;
    height: 1200px;
    overflow: hidden;
    background: var(--page-bg);
    font-family: "Arimo", Arial, sans-serif;
  }
  .canvas {
    position: relative;
    width: 1200px;
    height: 1200px;
  }
  .card {
    position: absolute;
    top: 306px;
    width: 380px;
    height: 588px;
    box-sizing: border-box;
    box-shadow: 0 4px 18px var(--card-shadow);
    overflow: hidden;
  }
  /* front side */
  .card-front {
    left: 190px;
    background: var(--card-white);
  }
  .card-front .brand {
    position: absolute;
    left: 24px;
    top: 30px;
    font-size: 33px;
    letter-spacing: -0.5px;
    color: var(--brand-grey);
    font-weight: 400;
  }
  .card-front .person {
    position: absolute;
    left: 72px;
    top: 150px;
  }
  .person-name {
    font-size: 24px;
    font-weight: 700;
    color: var(--text-dark);
    margin: 0;
  }
  .person-role {
    font-size: 14px;
    color: var(--text-grey);
    margin: 4px 0 0;
  }
  .contact-band {
    position: absolute;
    left: 0;
    right: 0;
    top: 302px;
    bottom: 0;
    background: linear-gradient(to bottom, var(--card-grey-top), var(--card-grey-bottom));
    border-top: 3px solid var(--accent-red);
  }
  .contact {
    position: absolute;
    left: 24px;
    top: 46px;
    font-size: 14px;
    line-height: 19px;
    color: var(--text-grey);
  }
  .contact p { margin: 0 0 18px; }
  /* back side */
  .card-back {
    left: 630px;
    background: linear-gradient(160deg, var(--back-grey-top), var(--back-grey-bottom));
    border: 10px solid var(--card-white);
  }
  .card-back .brand {
    position: absolute;
    left: 26px;
    bottom: 92px;
    display: flex;
    align-items: center;
    gap: 10px;
    font-size: 38px;
    letter-spacing: -0.5px;
    color: #4a4a4a;
  }
  .brand-square {
    width: 18px;
    height: 18px;
    background: var(--accent-red);
  }
</style>
</head>
<body>
<main class="canvas">
  <section class="card card-front" aria-label="Visitenkarte Vorderseite">
    <div class="brand">terbek wohnwerte</div>
    <div class="person">
      <p class="person-name">Jonas Terbek</p>
      <p class="person-role">Geschäftsführer</p>
    </div>
    <div class="contact-band">
      <div class="contact">
        <p>Lindenweg 12<br>D-35041 Talheim</p>
        <p>Fon: +49 (0)6421 5520410<br>Fax: +49 (0)6421 5520419</p>
        <p>www.terbek-wohnwerte.de<br>jt@terbek-wohnwerte.de</p>
      </div>
    </div>
  </section>

  <section class="card card-back" aria-label="Visitenkarte Rückseite">
    <div class="brand"><span class="brand-square"></span>terbek wohnwerte</div>
  </section>
</main>
</body>
</html>
```